oN Hand Plus Project

We are a wireless internet service provider (WISP). We are launching a new service to our customers called "oN Hand Plus". This new program will provide the following services to our customers as part of the $8.95 monthly service fee:
In-Home service calls are free
Provide WiFi Router
Router Support and Configuration
Free Cable Move (1 per year)
Cable Repair
Anti-Virus protection software
We will also be offering these services for additional charges:
Internet Security Suite $4.95 /month
Online Backup Storage - $4.99 /month
Target Market(s)
Current customers that use our internet service.
Industry/Entity Type
Wireless Internet
Look and feel

```html
<!DOCTYPE html>
<html lang="en">
<head>
<meta charset="utf-8">
<title>oN Hand Plus – Mesa Breeze Wireless</title>
<link href="https://fonts.googleapis.com/css2?family=Oswald:wght@500;600;700&display=swap" rel="stylesheet">
<style>
  :root {
    --blue-deep: #0a1f9e;
    --blue-mid: #1f3fd6;
    --blue-light: #3f6cf0;
    --red: #d4121f;
    --red-dark: #a80c16;
    --white: #ffffff;
    --skin: #e8a27c;
  }
  * { margin: 0; padding: 0; box-sizing: border-box; }
  html, body { width: 933px; height: 1200px; overflow: hidden; background: var(--blue-deep); }
  .flyer {
    position: relative;
    width: 933px;
    height: 1200px;
    overflow: hidden;
    background:
      radial-gradient(ellipse 60% 35% at 85% 55%, rgba(120,160,255,0.35), transparent 70%),
      radial-gradient(ellipse 70% 40% at 20% 75%, rgba(90,130,255,0.25), transparent 70%),
      linear-gradient(180deg, var(--blue-mid) 0%, var(--blue-light) 45%, var(--blue-mid) 75%, var(--blue-deep) 100%);
  }
  .artwork { position: absolute; left: 0; top: 0; display: block; }
  .artwork text {
    font-family: "Oswald", "Arial Narrow", sans-serif;
    font-weight: 600;
    fill: var(--white);
  }
  .artwork .headline { font-weight: 700; }
  .artwork .brand-name { fill: var(--blue-deep); font-weight: 600; }
  .services-box { fill: rgba(20, 40, 200, 0.35); stroke: var(--red); stroke-width: 2; }
  .dot { fill: var(--red); }
  .price-badge { fill: var(--red); }
  .divider { stroke: var(--red); stroke-width: 4; }
  .footer-band { fill: url(#bandFill); }
  .brand-oval { fill: var(--white); }
  .brand-mark { fill: var(--blue-deep); }
</style>
</head>
<body>
<main class="flyer">
  <svg class="artwork" width="933" height="1200" viewBox="0 0 933 1200" xmlns="http://www.w3.org/2000/svg">
    <defs>
      <filter id="textShadow" x="-5%" y="-20%" width="110%" height="150%">
        <feDropShadow dx="3" dy="4" stdDeviation="3" flood-color="#000028" flood-opacity="0.6"/>
      </filter>
      <linearGradient id="bandFill" x1="0" y1="0" x2="0" y2="1">
        <stop offset="0" stop-color="#d4121f"/>
        <stop offset="1" stop-color="#a80c16"/>
      </linearGradient>
      <linearGradient id="handFill" x1="0" y1="0" x2="1" y2="1">
        <stop offset="0" stop-color="#f0b48f"/>
        <stop offset="0.6" stop-color="#e8a27c"/>
        <stop offset="1" stop-color="#c97d57"/>
      </linearGradient>
    </defs>

    <g filter="url(#textShadow)">
      <text class="kicker" x="65" y="143" font-size="68" textLength="780" lengthAdjust="spacingAndGlyphs">FOR YOU, OUR LOYAL CUSTOMERS...</text>
      <text class="headline" x="65" y="245" font-size="122" textLength="796" lengthAdjust="spacingAndGlyphs">oN Hand Plus</text>
      <text class="subline" x="56" y="288" font-size="36" textLength="826" lengthAdjust="spacingAndGlyphs">THE COMPLETE SERVICE PLAN TO COMPLIMENT YOUR INTERNET SERVICE</text>
    </g>

    <polygon class="services-box" points="82,309 891,309 891,944 88,958"/>

    <g filter="url(#textShadow)">
      <text x="73" y="384" font-size="38" textLength="793" lengthAdjust="spacingAndGlyphs">SERVICES IN OUR NEW “ON HAND PLUS” PACKAGE INCLUDE:</text>

      <circle class="dot" cx="86" cy="437" r="12"/>
      <text x="108" y="452" font-size="50" textLength="491" lengthAdjust="spacingAndGlyphs">FREE IN-HOME SERVICE CALLS</text>
      <circle class="dot" cx="87" cy="502" r="12"/>
      <text x="109" y="517" font-size="50" textLength="300" lengthAdjust="spacingAndGlyphs">FREE WIFI ROUTER</text>
      <circle class="dot" cx="89" cy="566" r="12"/>
      <text x="111" y="581" font-size="50" textLength="758" lengthAdjust="spacingAndGlyphs">FREE ROUTER SUPPORT, CONFIGURATION, &amp; SETUP</text>
      <circle class="dot" cx="91" cy="630" r="12"/>
      <text x="113" y="645" font-size="50" textLength="522" lengthAdjust="spacingAndGlyphs">FREE CABLE MOVE (1 PER YEAR)</text>
      <circle class="dot" cx="93" cy="692" r="12"/>
      <text x="115" y="707" font-size="50" textLength="341" lengthAdjust="spacingAndGlyphs">FREE CABLE REPAIRS</text>
      <circle class="dot" cx="94" cy="754" r="12"/>
      <text x="116" y="769" font-size="50" textLength="673" lengthAdjust="spacingAndGlyphs">FREE ANTI-VIRUS PROTECTION SOFTWARE</text>
    </g>

    <g transform="rotate(-8 782 649)">
      <ellipse class="price-badge" cx="782" cy="649" rx="99" ry="61"/>
      <text x="782" y="625" font-size="28" text-anchor="middle">ONLY</text>
      <text x="782" y="656" font-size="30" text-anchor="middle">$8.95</text>
      <text x="782" y="686" font-size="28" text-anchor="middle">PER MONTH</text>
    </g>

    <line class="divider" x1="82" y1="802" x2="861" y2="777"/>

    <g filter="url(#textShadow)">
      <text x="116" y="839" font-size="42" textLength="721" lengthAdjust="spacingAndGlyphs">MORE SERVICES FOR ADDITIONAL FEES INCLUDE:</text>
      <circle class="dot" cx="138" cy="880" r="8"/>
      <text x="154" y="893" font-size="34" textLength="492" lengthAdjust="spacingAndGlyphs">INTERNET SECURITY SUITE $4.95 /MONTH</text>
      <circle class="dot" cx="138" cy="915" r="8"/>
      <text x="154" y="928" font-size="34" textLength="500" lengthAdjust="spacingAndGlyphs">ONLINE BACKUP STORAGE - $4.99 /MONTH</text>
    </g>

    <rect class="footer-band" x="0" y="1060" width="933" height="64"/>
    <path d="M0 905 H120 Q172 905 172 960 V1062 H0 Z" fill="url(#handFill)" role="img" aria-label="Photo of a hand giving a thumbs up"/>

    <text x="84" y="1106" font-size="44" textLength="359" lengthAdjust="spacingAndGlyphs" filter="url(#textShadow)">WWW.MESABREEZEWIFI.NET</text>

    <ellipse class="brand-oval" cx="732" cy="1081" rx="205" ry="118"/>
    <circle class="brand-mark" cx="586" cy="1081" r="11"/>
    <text class="brand-name" x="750" y="1072" font-size="36" text-anchor="middle">MESA BREEZE</text>
    <text class="brand-name" x="750" y="1112" font-size="36" text-anchor="middle">WIRELESS</text>
  </svg>
</main>
</body>
</html>
```